KVT Calculator

We have a calculator already created however the design seems to be very boring and bland. The calculators goal is to show graphic designers, web development firms, pr agencies, marketing firms how much revenue they can potentially make by offering a managed social media solution to their clients.

We want a great designer to make the calculator appealing to our audience.

It is an amazing offer and opportunity however I do not believe the current design does it justice

you can view and play with calculator live at http://sandbox.plivoran.com/tkna/

```html
<!DOCTYPE html>
<html lang="en">
<head>
<meta charset="utf-8">
<title>Revenue Calculator</title>
<link rel="stylesheet" href="https://fonts.googleapis.com/css2?family=Open+Sans:wght@300;400;600;700&display=swap">
<style>
  :root {
    --page-bg: #e9e9e9;
    --sheet: #ffffff;
    --rail-top: #343c55;
    --rail-bottom: #20273a;
    --track-dark: #0d3a52;
    --track-fill: #2a8fb8;
    --tick: #6d7489;
    --column: #2a2b2d;
    --column-divider: #333436;
    --basic: #2a8ab0;
    --pro: #ffa000;
    --label: #222222;
    --rule: #222222;
    --footer: #555555;
    --white: #ffffff;
    --btn-top: #8a929c;
    --btn-bottom: #5c636c;
  }
  * { box-sizing: border-box; margin: 0; padding: 0; }
  html, body { width: 1200px; height: 708px; overflow: hidden; }
  body {
    background: var(--page-bg);
    font-family: "Open Sans", Arial, sans-serif;
    position: relative;
  }
  .sheet {
    position: absolute; left: 109px; top: 77px; width: 980px; height: 334px;
    background: var(--sheet);
    box-shadow: 0 4px 12px rgba(0,0,0,.18);
  }
  .total-bar {
    position: absolute; left: 280px; top: 413px; width: 807px; height: 86px;
    background: var(--footer);
    color: var(--white);
    font-weight: 400; font-size: 33px;
    display: flex; align-items: center; justify-content: center;
    padding-left: 16px; padding-top: 2px;
    text-shadow: 0 1px 2px rgba(0,0,0,.4);
    box-shadow: 0 4px 10px rgba(0,0,0,.2);
    z-index: 1;
  }
  .total-bar strong { font-weight: 700; margin-left: 9px; }

  .term-rail {
    position: absolute; left: 122px; top: 58px; width: 157px; height: 441px;
    background: linear-gradient(var(--rail-top), var(--rail-bottom));
    border: 1px solid #161b28; border-radius: 4px;
    box-shadow: 0 4px 12px rgba(0,0,0,.3);
    z-index: 2;
  }
  .term-label {
    position: absolute; left: 5px; top: 7px; width: 145px; height: 41px;
    background: linear-gradient(#fbfbfb, #d6d6d6);
    border-radius: 5px;
    font-weight: 600; font-size: 19px; color: #1f1f1f;
    display: flex; align-items: center; justify-content: center;
  }
  .term-slider { position: absolute; left: 0; top: 0; }

  .row-label {
    position: absolute; left: 297px; width: 210px;
    font-weight: 700; font-size: 16px; color: var(--label);
    padding-left: 10px;
  }
  .row-rule { position: absolute; left: 297px; width: 210px; height: 1px; background: var(--rule); }

  .plan {
    position: absolute; top: 61px; width: 176px; height: 364px;
    background: var(--column);
    border-radius: 4px;
    box-shadow: 0 3px 8px rgba(0,0,0,.35);
    color: var(--white);
    z-index: 3;
  }
  .plan-basic { left: 517px; --accent: var(--basic); }
  .plan-pro { left: 709px; --accent: var(--pro); }
  .plan-enterprise { left: 899px; --accent: var(--basic); }
  .plan-name {
    height: 63px; background: var(--accent);
    border-radius: 4px 4px 0 0;
    display: flex; align-items: center; justify-content: center;
    font-weight: 600; font-size: 21px;
  }
  .plan-row {
    border-bottom: 1px solid var(--column-divider);
    display: flex; align-items: center; justify-content: center;
    position: relative; font-size: 22px; font-weight: 600;
  }
  .plan-row.clients { height: 67px; }
  .plan-row.cost { height: 71px; }
  .plan-row.price { height: 71px; }
  .plan-row.profit { height: 64px; padding-top: 12px; font-weight: 700; font-size: 20px; border-bottom: none; }
  .step {
    position: absolute; top: 16px; width: 37px; height: 32px;
    background: linear-gradient(var(--btn-top), var(--btn-bottom));
    border-radius: 5px;
    font-size: 26px; font-weight: 700; line-height: 30px; text-align: center;
    box-shadow: 0 1px 2px rgba(0,0,0,.5);
  }
  .plan-row.price .step { top: 18px; }
  .step-minus { left: 0; }
  .step-plus { right: 0; }
  .plan-accent-strip {
    position: absolute; left: 4px; right: 4px; bottom: 12px; height: 13px;
    background: var(--accent); border-radius: 2px;
  }
</style>
</head>
<body>
  <div class="sheet"></div>

  <div class="row-label" style="top:147px">Clients per month:</div>
  <div class="row-rule" style="top:189px"></div>
  <div class="row-label" style="top:217px">You pay:</div>
  <div class="row-rule" style="top:261px"></div>
  <div class="row-label" style="top:288px">Your client pays:</div>
  <div class="row-rule" style="top:332px"></div>
  <div class="row-label" style="top:361px">Monthly profit (year 8):</div>

  <div class="plan plan-basic">
    <div class="plan-name">BASIC</div>
    <div class="plan-row clients"><span class="step step-minus">−</span>1<span class="step step-plus">+</span></div>
    <div class="plan-row cost">$197</div>
    <div class="plan-row price"><span class="step step-minus">−</span>$297<span class="step step-plus">+</span></div>
    <div class="plan-row profit">$9,600</div>
    <div class="plan-accent-strip"></div>
  </div>

  <div class="plan plan-pro">
    <div class="plan-name">PRO</div>
    <div class="plan-row clients"><span class="step step-minus">−</span>1<span class="step step-plus">+</span></div>
    <div class="plan-row cost">$297</div>
    <div class="plan-row price"><span class="step step-minus">−</span>$497<span class="step step-plus">+</span></div>
    <div class="plan-row profit">$19,200</div>
    <div class="plan-accent-strip"></div>
  </div>

  <div class="plan plan-enterprise">
    <div class="plan-name">ENTERPRISE</div>
    <div class="plan-row clients"><span class="step step-minus">−</span>1<span class="step step-plus">+</span></div>
    <div class="plan-row cost">$2500</div>
    <div class="plan-row price"><span class="step step-minus">−</span>$4000<span class="step step-plus">+</span></div>
    <div class="plan-row profit">$144,000</div>
    <div class="plan-accent-strip"></div>
  </div>

  <div class="total-bar">Monthly profit by the end of year 8:<strong>$172,800</strong></div>

  <div class="term-rail">
    <div class="term-label">TERM (YRS)</div>
    <svg class="term-slider" width="157" height="441" viewBox="0 0 157 441" aria-label="Term slider set to 8 years">
      <g stroke="var(--tick)" stroke-width="2">
        <line x1="56" y1="105" x2="104" y2="105"/>
        <line x1="56" y1="140" x2="104" y2="140"/>
        <line x1="56" y1="175" x2="104" y2="175"/>
        <line x1="56" y1="208" x2="104" y2="208"/>
        <line x1="56" y1="242" x2="104" y2="242"/>
        <line x1="56" y1="276" x2="104" y2="276"/>
        <line x1="56" y1="310" x2="104" y2="310"/>
        <line x1="56" y1="345" x2="104" y2="345"/>
        <line x1="56" y1="379" x2="104" y2="379"/>
      </g>
      <rect x="72" y="88" width="16" height="313" rx="8" fill="var(--track-dark)"/>
      <rect x="72" y="137" width="16" height="264" rx="8" fill="var(--track-fill)"/>
      <circle cx="79" cy="137" r="19" fill="#ffffff" stroke="#c8c8c8" stroke-width="1"/>
      <circle cx="79" cy="137" r="9" fill="#9a9a9a" stroke="#7a7a7a" stroke-width="1"/>
    </svg>
  </div>
</body>
</html>
```